Tour operator needs simple coded WordPress site (updated extra payment for coding and guaranteed)

[update 9/7/2015]
If you design a new logo and it gets accepted, even if we use another template with your logo you will get $50
[update 8/7/2015]
Update on questions about dual-language
For dual languages we are happy to set up a second site with the same designs in a second language.
For the design aspect just allow the user to switch between languages with an icon.
For the coding, a replica of the site on a second server will do (to save messing around with multiple language plugins) - we will populate it with Chinese text
[original post]
Simple coded WordPress site for tours
You can choose to design only or design and code ($340 design, $150 bonus for coding)
Open design brief - use your creativity
Will be in 2 languages (English and Chinese) but design needs only to be in one language
Winning design will be chosen only from home page, but the winner must make a second standard template page when chosen at no extra cost.
Must be responsive design
We only need homepage and standard template page design and coding, we will populate the pages
You can use design ideas from our pamphlet if you like - attached
Only a sample logo and colors on website and pamphlet - feel free to change as the current ones seem restrictive
Current website framework only to give an idea of the number of pages and basic menu structure (no need to use existing navigation style or any style at all for that matter, open brief)
http://brightwaterlearningtrips.com.au/
Target Market(s)
Chinese parents of kids 10-14 (the kids will take the tour)
Industry/Entity Type
Tour
Number of Pages Required
2 page
Look and feel
Each slider illustrates characteristics of the customer's brand and the style your logo design should communicate.

```html
<!DOCTYPE html>
<html lang="en">
<head>
<meta charset="utf-8">
<title>Brightwater Learning Trips</title>
<link href="https://fonts.googleapis.com/css2?family=Poppins:wght@300;400;700&family=Dancing+Script:wght@500&display=swap" rel="stylesheet">
<style>
:root{
  --yellow:#f2c418;
  --green:#8cb84a;
  --blue:#2aa6d8;
  --orange:#f0a21c;
  --text:#6b6b6b;
  --white:#ffffff;
  --footer:#7fa954;
}
*{box-sizing:border-box;margin:0;padding:0}
html,body{width:802px;height:1200px;overflow:hidden;background:var(--white);font-family:'Poppins',sans-serif;color:var(--text)}
.page{position:relative;width:802px;height:1200px}
.site-header{position:absolute;left:0;top:0;width:802px;height:100px}
.brand{position:absolute;left:24px;top:14px;display:flex;align-items:center;gap:14px}
.brand-name{font-family:'Poppins',sans-serif;font-weight:700;font-size:23px;line-height:25px;color:var(--blue);text-transform:uppercase;width:200px}
.brand-dot{width:46px;height:46px;border-radius:50%;background:var(--blue)}
.stripe{position:absolute;left:300px;right:0}
.stripe-yellow{top:8px;height:12px;background:var(--yellow)}
.stripe-green{top:26px;height:12px;background:var(--green)}
.main-nav{position:absolute;left:300px;right:0;top:62px;height:30px;background:var(--blue);display:flex;justify-content:flex-end;align-items:center;gap:38px;padding-right:30px}
.main-nav a{color:var(--white);text-decoration:none;font-size:13px;letter-spacing:1px;text-transform:uppercase}
.hero{position:absolute;left:0;top:100px;width:802px;height:390px;background:linear-gradient(180deg,#c9dcec 0%,#8fb3cf 35%,#4f7f9c 60%,#2e5d74 100%)}
.hero-tagline{position:absolute;left:510px;top:220px;width:250px;font-family:'Dancing Script',cursive;font-size:27px;line-height:32px;color:var(--white)}
.slider-dots{position:absolute;left:0;right:0;top:472px;display:flex;justify-content:center;gap:8px}
.slider-dots span{width:10px;height:10px;border-radius:50%;background:#9fc3dc}
.slider-dots span.active{background:var(--white)}
.features{position:absolute;left:80px;top:530px;width:660px;display:flex;justify-content:space-between}
.feature{width:150px;text-align:center}
.feature-icon{width:92px;height:92px;margin:0 auto}
.feature p{margin-top:12px;font-size:9px;line-height:12px;text-align:left}
.intro{position:absolute;left:118px;top:820px;width:566px;text-align:center;font-size:13.5px;line-height:19px;font-weight:300}
.intro p{margin-bottom:19px}
.intro .highlight{color:var(--orange);font-weight:400}
.site-footer{position:absolute;left:0;top:1168px;width:802px;height:32px;background:var(--footer);color:var(--white);font-size:9px;display:flex;align-items:center;justify-content:center}
</style>
</head>
<body>
<div class="page">
  <header class="site-header">
    <div class="brand">
      <div class="brand-name">Brightwater Learning Trips</div>
      <div class="brand-dot"></div>
    </div>
    <div class="stripe stripe-yellow"></div>
    <div class="stripe stripe-green"></div>
    <nav class="main-nav">
      <a href="#">Menu</a><a href="#">Tours</a><a href="#">Contact</a><a href="#">About us</a>
    </nav>
  </header>

  <section class="hero" role="img" aria-label="Aerial photograph of a harbour city skyline with an opera house on the waterfront">
    <div class="hero-tagline">Educational, safe, culturally enlightening and fun.</div>
  </section>
  <div class="slider-dots"><span></span><span class="active"></span><span></span><span></span></div>

  <section class="features">
    <div class="feature">
      <svg class="feature-icon" viewBox="0 0 92 92"><circle cx="46" cy="46" r="44" fill="var(--orange)"/><circle cx="46" cy="46" r="36" fill="none" stroke="#fff" stroke-width="2"/><path d="M46 24c-9 0-15 7-15 15 0 11 15 28 15 28s15-17 15-28c0-8-6-15-15-15z" fill="#fff"/><circle cx="46" cy="39" r="5" fill="var(--orange)"/></svg>
      <p>In this premium cultural and educational tour to Australian cities, students enjoy culturally enlightening visits to schools, museums, parks and local families.</p>
    </div>
    <div class="feature">
      <svg class="feature-icon" viewBox="0 0 92 92"><circle cx="46" cy="46" r="44" fill="var(--orange)"/><circle cx="46" cy="46" r="36" fill="none" stroke="#fff" stroke-width="2"/><path d="M26 30c8-3 15-2 20 3v33c-5-5-12-6-20-3z M66 30c-8-3-15-2-20 3v33c5-5 12-6 20-3z" fill="#fff" stroke="var(--orange)" stroke-width="1.5"/></svg>
      <p>Learn about Australia's political and legal systems and find out about its educational institutions and history.</p>
    </div>
    <div class="feature">
      <svg class="feature-icon" viewBox="0 0 92 92"><circle cx="46" cy="46" r="44" fill="var(--orange)"/><circle cx="46" cy="46" r="36" fill="none" stroke="#fff" stroke-width="2"/><path d="M46 22c-10 0-17 7-17 16 0 7 5 10 8 15v6h18v-6c3-5 8-8 8-15 0-9-7-16-17-16z" fill="#fff"/><rect x="38" y="62" width="16" height="4" fill="#fff"/><rect x="40" y="68" width="12" height="4" fill="#fff"/></svg>
      <p>Learn about the unique wildlife and geography of this beautiful continent.</p>
    </div>
    <div class="feature">
      <svg class="feature-icon" viewBox="0 0 92 92"><circle cx="46" cy="46" r="44" fill="var(--orange)"/><circle cx="46" cy="46" r="36" fill="none" stroke="#fff" stroke-width="2"/><path d="M46 24l6 13 14 1-11 9 4 14-13-8-13 8 4-14-11-9 14-1z" fill="#fff"/></svg>
      <p>Find out about the rich and multicultural heritage of Australia as it is reflected in the arts.</p>
    </div>
  </section>

  <section class="intro">
    <p>At the <span class="highlight">Brightwater Learning Trips</span> we are passionate about educational travel and providing opportunities for students to learn more about Australia and gain a deeper understanding of the culture. The out of classroom experience gained on our trips is invaluable.</p>
    <p>Taking the <span class="highlight">Brightwater Learning Trips</span> tour is easy because our team of dedicated experts assists every step of the way – from meticulously planning the curriculum to ensuring every detail of your trip is accommodating you on tour.</p>
    <p>We inspect every hotel, visit every attraction, evaluate every teacher and sample every restaurant. Wherever you go on tour, we've been there. And we always listen to our travelers. We are known for our exceptional standards.</p>
    <p>We have an extensive team of specialists to help you with all your travel needs. We have staff that have travelled around Australia and can use their first-hand knowledge to help make your trip educational, enjoyable and hassle free.</p>
  </section>

  <footer class="site-footer">Copyright © 2015 Brightwater Learning Trips</footer>
</div>
</body>
</html>
```